Business Card Design needed for logo design project

This project is linked to Logo: brand identity for modern furniture design studio..

Our company needs a Business Card Design. Please refer to our original project in the link above.

Industry/Entity Type

Business

```html
<!DOCTYPE html>
<html lang="en">
<head>
<meta charset="utf-8">
<title>Vellor Business Card</title>
<link href="https://fonts.googleapis.com/css2?family=Questrial&display=swap" rel="stylesheet">
<style>
  :root {
    --backdrop: #ecebe9;
    --card-white: #ffffff;
    --card-grey: #cdcac6;
    --rule: #b9b5b1;
    --ink: #1c1c1c;
    --ink-soft: #2a2a2a;
  }
  * { margin: 0; padding: 0; box-sizing: border-box; }
  html, body {
    width: 1200px; height: 676px; overflow: hidden;
    background: var(--backdrop);
    font-family: "Questrial", "Century Gothic", sans-serif;
    color: var(--ink);
  }
  .canvas {
    width: 1200px; height: 676px;
    display: flex; align-items: center; justify-content: center;
  }
  .business-card {
    width: 700px; height: 400px;
    background: var(--card-grey);
    position: relative;
    box-shadow: 0 10px 30px rgba(0,0,0,0.15);
  }
  .brand-band {
    height: 170px;
    background: var(--card-white);
    border-bottom: 2px solid var(--rule);
    display: flex; align-items: center;
    padding-left: 70px;
  }
  .brand-name {
    font-size: 96px;
    font-weight: 400;
    letter-spacing: 2px;
    line-height: 1;
    color: var(--ink);
  }
  .owner-block {
    position: absolute; left: 50px; top: 205px;
    display: flex; gap: 14px;
  }
  .owner-block .icon { margin-top: 30px; }
  .owner-name { font-size: 19px; letter-spacing: 0.5px; }
  .owner-phone { font-size: 19px; margin-top: 10px; }
  .contact-list {
    position: absolute; left: 400px; top: 245px;
    list-style: none;
  }
  .contact-list li {
    display: flex; align-items: center; gap: 14px;
    font-size: 19px; color: var(--ink-soft);
    height: 26px;
  }
  .contact-list li.plain { padding-left: 32px; }
  .icon { width: 18px; height: 18px; flex: none; }
  .icon path, .icon circle, .icon rect, .icon line { stroke: var(--ink); fill: none; stroke-width: 1.5; }
  .icon .solid { fill: var(--ink); stroke: none; }
</style>
</head>
<body>
<main class="canvas">
  <article class="business-card">
    <header class="brand-band">
      <span class="brand-name">Vellor</span>
    </header>

    <section class="owner-block">
      <svg class="icon" viewBox="0 0 18 18" aria-hidden="true">
        <path class="solid" d="M4 2 L7 2 L8 6 L6 7.5 C7 10 8 11 10.5 12 L12 10 L16 11 L16 14 C16 15 15 16 14 16 C8 16 2 10 2 4 C2 3 3 2 4 2 Z"/>
      </svg>
      <div>
        <p class="owner-name">YOUR NAME</p>
        <p class="owner-phone">555-201-4830</p>
      </div>
    </section>

    <ul class="contact-list">
      <li>
        <svg class="icon" viewBox="0 0 18 18" aria-hidden="true">
          <path d="M9 17 C9 17 3 10 3 6.5 A6 6 0 0 1 15 6.5 C15 10 9 17 9 17 Z"/>
          <circle cx="9" cy="6.5" r="2"/>
        </svg>
        <span>418 Alder Lane</span>
      </li>
      <li class="plain"><span>Bay Area CA-75021</span></li>
      <li>
        <svg class="icon" viewBox="0 0 18 18" aria-hidden="true">
          <circle cx="9" cy="9" r="7.5"/>
          <path d="M9 1.5 C5 5 5 13 9 16.5 M9 1.5 C13 5 13 13 9 16.5"/>
          <line x1="1.5" y1="9" x2="16.5" y2="9"/>
          <line x1="3" y1="5" x2="15" y2="5"/>
          <line x1="3" y1="13" x2="15" y2="13"/>
        </svg>
        <span>www.vellor.com</span>
      </li>
      <li>
        <svg class="icon" viewBox="0 0 18 18" aria-hidden="true">
          <rect x="1.5" y="4" width="15" height="10"/>
          <path d="M1.5 4 L9 10 L16.5 4"/>
        </svg>
        <span>info@vellor.com</span>
      </li>
    </ul>
  </article>
</main>
</body>
</html>
```